Veloran Prime is a new over the counter dietary supplement

we are looking for a professional design to attract the eye initally, clean, simple, clinical.

Target Market(s)

20 - 70 year old inflamation sufferers, painful joints, etc

Industry/Entity Type

Supplement

Requirements
Must have
• the words....curcumin, Veloran Prime, oral liquid, 100ml, AustL5807, space for barcode, space for lots of printing like instructions for use etc. using turmeric orange and leaf green colouring.
Nice to have
• can have turmeric flower, or green leaf/petals, fine line dividing sections, matt finish,

```html
<!DOCTYPE html>
<html lang="en">
<head>
<meta charset="utf-8">
<title>Veloran Prime – Oral Liquid Label</title>
<link href="https://fonts.googleapis.com/css2?family=Arimo:wght@400;700&display=swap" rel="stylesheet">
<style>
  :root {
    --page: #ece6dc;
    --turmeric: #e8920e;
    --turmeric-deep: #d97a06;
    --band: #f0b418;
    --leaf: #2f5f1f;
    --rule: #79a866;
    --ink: #1f1f1f;
    --navy: #1c2a86;
    --paper-a: #fbfcf5;
    --paper-b: #e9f1dc;
  }
  * { box-sizing: border-box; margin: 0; padding: 0; }
  html, body { width: 1200px; height: 600px; overflow: hidden; }
  body {
    background: var(--page);
    font-family: "Arimo", Arial, sans-serif;
    color: var(--ink);
    position: relative;
  }
  .label {
    position: absolute;
    left: 132px; top: 120px;
    width: 934px; height: 360px;
    background: var(--paper-a);
    box-shadow: 0 2px 8px rgba(0,0,0,.18);
  }
  .band {
    position: absolute; left: 0; width: 100%; height: 12px;
    background: var(--band);
    border-top: 1px solid var(--turmeric-deep);
    border-bottom: 1px solid var(--turmeric-deep);
  }
  .band--top { top: 0; }
  .band--bottom { bottom: 0; }
  .panel {
    position: absolute; top: 12px; bottom: 12px;
    border: 1px solid var(--rule);
  }
  .panel__art {
    position: absolute; inset: 0;
    background: linear-gradient(160deg, var(--paper-a) 0%, var(--paper-b) 55%, var(--paper-a) 100%);
  }
  .panel--left { left: 0; width: 332px; }
  .panel--centre { left: 331px; width: 259px; }
  .panel--right { left: 589px; right: 0; }
  .panel__divider {
    position: absolute; left: 0; right: 0; height: 1px; background: var(--rule);
  }
  .panel--left .panel__divider { top: 244px; }
  .panel--right .panel__divider { top: 247px; }

  .centre { position: relative; text-align: center; height: 100%; }
  .brand-row {
    display: flex; align-items: center; justify-content: center; gap: 10px;
    padding-top: 10px;
  }
  .brand {
    display: flex; align-items: center; gap: 5px;
    font-weight: 700; font-size: 20px; color: var(--leaf);
  }
  .brand__dot { width: 14px; height: 14px; border-radius: 50%; background: var(--turmeric); }
  .category { font-weight: 700; font-size: 16px; line-height: 19px; color: var(--leaf); }
  .category .hl { color: var(--turmeric); }
  .product-name {
    margin-top: 12px;
    font-weight: 700; font-size: 38px; line-height: 40px;
    color: var(--turmeric);
    text-shadow: 1px 1px 0 rgba(90,60,0,.35);
  }
  .claims {
    font-size: 18px; line-height: 21.5px;
    word-spacing: 2px; letter-spacing: .2px;
  }
  .claims .hl { color: var(--turmeric); font-weight: 700; }
  .dose-note { font-size: 9px; line-height: 11px; }
  .volume { margin-top: 13px; font-weight: 700; font-size: 19px; line-height: 22px; }
  .listing { margin-top: 1px; font-weight: 700; font-size: 13px; line-height: 16px; }
  .format {
    position: absolute; left: 0; right: 0; bottom: 10px;
    font-weight: 700; font-size: 20px; word-spacing: 4px; color: var(--leaf);
  }
  .contact {
    position: absolute; left: 18px; top: 254px;
    font-weight: 700; font-size: 16px; line-height: 20px;
    letter-spacing: .5px; color: var(--navy);
  }
  .origin {
    position: absolute; left: 18px; top: 314px;
    font-weight: 700; font-size: 15px; letter-spacing: .5px; color: var(--ink);
  }
</style>
</head>
<body>
  <main class="label">
    <div class="band band--top"></div>

    <section class="panel panel--left">
      <div class="panel__art" role="img" aria-label="Faint pale green floral swirl background pattern"></div>
      <div class="panel__divider"></div>
    </section>

    <section class="panel panel--centre">
      <div class="panel__art" role="img" aria-label="Faint pale green floral swirl background pattern"></div>
      <div class="centre">
        <div class="brand-row">
          <div class="brand"><span class="brand__dot"></span>VHN</div>
          <p class="category"><span class="hl">Curcumin</span> Dietary<br>Supplement</p>
        </div>
        <h1 class="product-name">Veloran<br>Prime</h1>
        <div class="claims">
          <p>Oral liquid</p>
          <p>Powerful anti-inflammatory</p>
          <p>Potent antioxidant</p>
          <p><span class="hl">Curcumin</span> R7 Complex</p>
        </div>
        <p class="dose-note">(each 5ml contains 1200mg eqiv. to 5g dry rhizome)</p>
        <p class="volume">100ml</p>
        <p class="listing">AustL5807</p>
        <p class="format">liquid herbal extract</p>
      </div>
    </section>

    <section class="panel panel--right">
      <div class="panel__art" role="img" aria-label="Faint pale green floral swirl background pattern"></div>
      <div class="panel__divider"></div>
      <p class="contact">info@verdanthollow.com<br>www.verdanthollow.com</p>
      <p class="origin">Made in Australia.</p>
    </section>

    <div class="band band--bottom"></div>
  </main>
</body>
</html>
```